Simple and clean webdesign for personal homepage

Trying to create a simple and clean webdesign for my personal homepage. Going to use a static site builder with templates to build the site. I want it to have multiple pages - like an about me, blog and resume. I just need something very basic I can customize. I want the main colors to be purple, black and white. I am open to other color palettes too but since purple is my favorite color I want that to be one of the main colors.

The site be mostly text driven. Might have some images in the body text but I want the site design to be light and lean.

Industry/Entity Type

Personal Homepage.

Coding

Coded - Design and coding required

Number of Pages Required

1 page

Font styles to use
Sans Serif

Colors
6B429C
8869AF
B7A5CE
E3DAEB
F3F0F8

Requirements
Must have
• Clean design. Purple used as a color. HTML template.
Nice to have
• Responsive

```html
<!DOCTYPE html>
<html lang="en">
<head>
<meta charset="utf-8">
<title>Personal Homepage – Layouts</title>
<link href="https://fonts.googleapis.com/css2?family=Poppins:wght@300;400;500;600&display=swap" rel="stylesheet">
<style>
:root{
  --purple-deep:#6B429C;
  --purple:#8869AF;
  --purple-soft:#B7A5CE;
  --lavender:#E3DAEB;
  --mist:#F3F0F8;
  --ink:#111111;
  --text:#555555;
  --board:#F2F2F2;
  --white:#FFFFFF;
}
*{box-sizing:border-box;margin:0;padding:0}
html,body{width:709px;height:1200px;overflow:hidden;background:var(--board)}
body{font-family:'Poppins',sans-serif;color:var(--ink)}
.board{position:absolute;left:0;top:0;width:1484px;height:2512px;transform:scale(0.47776);transform-origin:0 0}
.page{position:absolute;width:633px;background:var(--white);overflow:hidden;box-shadow:0 0 6px rgba(0,0,0,.05)}
.page--home{left:83px;top:62px;height:2341px}
.page--blog{left:770px;top:62px;height:977px}
.page--post{left:770px;top:1117px;height:1195px}
.abs{position:absolute}

/* header */
.page-head{position:absolute;left:0;top:0;width:633px;background:linear-gradient(160deg,#EEEAF5 0%,var(--mist) 50%,#ECE7F3 100%)}
.page-head--hero{height:325px}
.page-head--inner{height:121px}
.brand{position:absolute;left:52px;top:14px;font-size:16px;font-weight:400;color:var(--ink)}
.nav{position:absolute;top:18px;display:flex;gap:0;font-size:9.5px;font-weight:400}
.nav span{margin-right:25px}
.nav .is-active{color:var(--purple-deep);text-decoration:underline;text-underline-offset:3px}
.page-title{position:absolute;top:72px;width:100%;text-align:center;font-size:19px;font-weight:600}

.hero-greet{position:absolute;top:131px;width:100%;text-align:center;font-size:13px}
.hero-title{position:absolute;top:154px;width:100%;text-align:center;font-size:19px;font-weight:600;line-height:24px}
.btn{display:inline-block;background:var(--purple-deep);color:var(--white);font-size:8px;text-align:center;border-radius:1px}
.hero-btn{position:absolute;left:275px;top:216px;width:83px;height:22px;line-height:22px}

/* about */
.about{position:absolute;left:0;top:325px;width:633px;height:165px;background:var(--purple)}
.about h2{position:absolute;left:56px;top:42px;font-size:19px;font-weight:400;color:var(--white);border-bottom:2px solid var(--white);padding-bottom:1px}
.about p{position:absolute;top:50px;width:188px;font-size:8px;line-height:13.5px;color:var(--white);font-weight:300}

/* sections */
.section{position:absolute;left:0;width:633px}
.section--white{background:var(--white)}
.section--mist{background:var(--mist)}
.sec-title{position:absolute;width:100%;text-align:center;font-size:19px;font-weight:500}
.sec-title span{border-bottom:2px solid var(--purple-deep);padding-bottom:1px}
.sec-desc{position:absolute;left:130px;width:373px;text-align:center;font-size:7.5px;line-height:15px;color:#333}

.work-card{position:absolute;top:132px;width:159px;height:148px;background:var(--white);box-shadow:0 0 5px rgba(0,0,0,.12);padding:14px 10px}
.work-card h3{font-size:11.5px;font-weight:500;margin-top:8px}
.work-card p{font-size:7px;line-height:11.5px;color:var(--text);margin-top:6px}

.skill{position:absolute;width:223px}
.skill-label{display:flex;justify-content:space-between;font-size:8.5px;padding:0 7px 0 1px}
.skill-track{margin-top:7px;height:10px;border-radius:5px;background:var(--purple-soft);overflow:hidden}
.skill-fill{height:100%;border-radius:5px;background:var(--purple-deep)}

.exp{position:absolute;left:0;width:633px}
.exp-date{position:absolute;left:54px;font-size:7px;color:var(--purple-deep)}
.exp-title{position:absolute;left:54px;top:11px;font-size:10.5px;font-weight:500;line-height:14px;width:210px}
.exp-dot{position:absolute;left:311px;top:-4px;width:11px;height:11px;border:1.5px solid var(--purple);border-radius:50%;background:var(--white)}
.exp-text{position:absolute;left:378px;top:11px;width:205px;font-size:7px;line-height:12.8px;color:#333}
.timeline-line{position:absolute;left:316px;width:1px;background:#C9C2D3}

.mini-card{position:absolute;top:90px;width:168px;height:127px;background:var(--white);box-shadow:0 0 5px rgba(0,0,0,.1);padding:10px 14px}
.date{font-size:7px;color:var(--purple-deep);display:flex;align-items:center;gap:3px}
.date i{display:inline-block;width:6px;height:6px;background:var(--purple-deep);border-radius:1px}
.card-title{font-size:9.5px;font-weight:500;line-height:12px;margin-top:6px}
.card-text{font-size:7px;line-height:11.5px;color:var(--text);margin-top:5px}
.more{font-size:7px;color:var(--purple-deep);font-weight:500;margin-top:4px}

/* contact */
.contact{position:absolute;left:0;top:1910px;width:633px;height:254px}
.contact-form{position:absolute;left:0;top:0;width:345px;height:254px;background:linear-gradient(135deg,#EDEDED 0%,#F7F7F7 50%,#E6E6E6 100%)}
.contact-info{position:absolute;left:345px;top:0;width:288px;height:254px;background:linear-gradient(135deg,#A48ECA 0%,#9C85C2 100%)}
.contact h2{position:absolute;font-size:19px;font-weight:500;top:36px}
.contact-form h2{left:59px}
.contact-form h2::after,.contact-info h2::after{content:"";display:block;width:28px;height:2px;background:var(--purple-deep);margin-top:2px}
.contact-info h2{left:65px;color:var(--white)}
.contact-info h2::after{background:var(--white)}
.field{position:absolute;height:23px;background:var(--white);font-size:6.5px;color:#333;padding:8px 6px}
.submit{position:absolute;left:59px;top:188px;width:86px;height:24px;line-height:24px;background:var(--purple-deep);color:var(--white);font-size:7.5px;text-align:center}
.info-label{position:absolute;left:64px;top:80px;font-size:8.5px;font-weight:500;color:var(--white)}
.info-row{position:absolute;left:64px;display:flex;align-items:center;gap:7px;color:var(--white)}
.info-icon{width:24px;height:24px;border-radius:50%;background:var(--white);display:flex;align-items:center;justify-content:center}
.info-row small{display:block;font-size:7px;font-weight:300;line-height:11px}
.info-row b{display:block;font-size:9px;font-weight:500;line-height:11px}

/* footer */
.site-foot{position:absolute;left:0;width:633px;background:var(--purple);color:var(--white);text-align:center}
.foot-brand{position:absolute;top:30px;width:100%;font-size:26px;font-weight:300}
.foot-nav{position:absolute;top:78px;width:100%;display:flex;justify-content:center;gap:24px;font-size:8.5px}
.foot-copy{position:absolute;top:106px;width:100%;font-size:7.5px;font-weight:300}
.foot-social{position:absolute;top:134px;width:100%;display:flex;justify-content:center;gap:6px}
.foot-social span{width:20px;height:20px;border-radius:50%;background:var(--white)}

/* blog grid */
.post-card{position:absolute;width:168px}
.photo{display:block;width:168px;height:128px}
.post-card .date{margin-top:8px}
.post-card .card-text{margin-top:6px}
.post-card .btn{width:83px;height:22px;line-height:22px;margin-top:9px}
.pager{position:absolute;top:733px;left:270px;display:flex;gap:4px}
.pager span{width:16px;height:16px;border:1px solid #ddd;font-size:8px;text-align:center;line-height:14px}
.pager .is-current{background:var(--purple-deep);color:var(--white);border-color:var(--purple-deep)}

/* single post */
.post-meta{position:absolute;left:53px;top:162px;display:flex;gap:14px;font-size:8.5px}
.post-title{position:absolute;left:52px;top:184px;font-size:20.5px;font-weight:500;line-height:23px}
.post-body{position:absolute;left:53px;width:527px;font-size:8px;line-height:17.8px;color:#444}
</style>
</head>
<body>
<div class="board">

  <!-- HOME PAGE -->
  <section class="page page--home">
    <header class="page-head page-head--hero">
      <div class="brand">Logo</div>
      <nav class="nav" style="left:236px"><span class="is-active">Home</span><span>About Me</span><span>Blog</span><span>Resume</span><span>My Work</span><span>Contact</span></nav>
      <p class="hero-greet">Hi, I’m Daniel Harper</p>
      <h1 class="hero-title">An independent software contractor,<br>architect &amp; tech trainer</h1>
      <span class="btn hero-btn">View Resume</span>
    </header>

    <section class="about">
      <h2>About Me</h2>
      <p style="left:179px">Lorem ipsum dolor sit amet, cotetur adipiscing elit, sed do eiusmod tempor iidunt ut labore et dolore maa aliqua. Quis ipsm suspendisse ultrices gravida. Risus mdo viverra maecenas accumsan lacus vel facilisis.</p>
      <p style="left:389px">Lorem ipsum dolor sit amet, cotetur adipiscing elit, sed do eiusmod tempor iidunt ut labore et dolore maa aliqua. Quis ipsm suspendisse ultrices gravida. Risus mdo viverra maecenas accumsan lacus vel facilisis.</p>
    </section>

    <section class="section section--white" style="top:490px;height:330px">
      <h2 class="sec-title" style="top:46px"><span>Our Works</span></h2>
      <p class="sec-desc" style="top:83px">Lorem ipsum dolor sit amet, consectetur adipiscing elit, sed do eiusmod tempor incididunt ut labore et dolore magna aliqua. Quis ipsum suspendisse ultrices gravida.</p>
      <article class="work-card" style="left:62px">
        <svg width="30" height="30" viewBox="0 0 30 30" fill="none" stroke="#6B429C" stroke-width="1.3"><path d="M4 26 L20 10"/><circle cx="23" cy="7" r="4"/><path d="M4 4 L26 26"/><path d="M3 7 L7 3"/></svg>
        <h3>Finibus Bonorum et</h3>
        <p>Lorem ipsum dolor simet, consectetur adipid do eiusmod tempor incididunt ut labolore magna aliqua. Quis ipsum suspendices gravida. Risus commodo viverra maecenas accumsan lacus vel facilisis.</p>
      </article>
      <article class="work-card" style="left:237px">
        <svg width="30" height="30" viewBox="0 0 30 30" fill="none" stroke="#6B429C" stroke-width="1.3"><circle cx="15" cy="15" r="11" stroke-dasharray="4 2"/><circle cx="15" cy="15" r="6"/><path d="M12 15 L14 17 L18 13"/></svg>
        <h3>Finibus Bonorum et</h3>
        <p>Lorem ipsum dolor simet, consectetur adipid do eiusmod tempor incididunt ut labolore magna aliqua. Quis ipsum suspendices gravida. Risus commodo viverra maecenas accumsan lacus vel facilisis.</p>
      </article>
      <article class="work-card" style="left:412px">
        <svg width="30" height="30" viewBox="0 0 30 30" fill="none" stroke="#6B429C" stroke-width="1.3"><path d="M15 3 L23 6 V12 C23 17 19 20 15 21 C11 20 7 17 7 12 V6 Z"/><path d="M11 12 L14 15 L19 9"/><path d="M2 24 H10 L16 27 L28 22"/></svg>
        <h3>Finibus Bonorum et</h3>
        <p>Lorem ipsum dolor simet, consectetur adipid do eiusmod tempor incididunt ut labolore magna aliqua. Quis ipsum suspendices gravida. Risus commodo viverra maecenas accumsan lacus vel facilisis.</p>
      </article>
    </section>

    <section class="section section--mist" style="top:820px;height:325px">
      <h2 class="sec-title" style="top:36px"><span>Skills</span></h2>
      <p class="sec-desc" style="top:73px">Lorem ipsum dolor sit amet, consectetur adipiscing elit, sed do eiusmod tempor incididunt ut labore et dolore magna aliqua. Quis ipsum suspendisse ultrices gravida.</p>
      <div class="skill" style="left:76px;top:122px"><div class="skill-label"><span>Skill 1</span><span>80%</span></div><div class="skill-track"><div class="skill-fill" style="width:79%"></div></div></div>
      <div class="skill" style="left:76px;top:167px"><div class="skill-label"><span>Skill 2</span><span>75%</span></div><div class="skill-track"><div class="skill-fill" style="width:70%"></div></div></div>
      <div class="skill" style="left:76px;top:212px"><div class="skill-label"><span>Skill 3</span><span>75%</span></div><div class="skill-track"><div class="skill-fill" style="width:70%"></div></div></div>
      <div class="skill" style="left:76px;top:257px"><div class="skill-label"><span>Skill 4</span><span>90%</span></div><div class="skill-track"><div class="skill-fill" style="width:91%"></div></div></div>
      <div class="skill" style="left:334px;top:122px"><div class="skill-label"><span>Skill 5</span><span>80%</span></div><div class="skill-track"><div class="skill-fill" style="width:79%"></div></div></div>
      <div class="skill" style="left:334px;top:167px"><div class="skill-label"><span>Skill 6</span><span>85%</span></div><div class="skill-track"><div class="skill-fill" style="width:84%"></div></div></div>
      <div class="skill" style="left:334px;top:212px"><div class="skill-label"><span>Skill 7</span><span>80%</span></div><div class="skill-track"><div class="skill-fill" style="width:79%"></div></div></div>
      <div class="skill" style="left:334px;top:257px"><div class="skill-label"><span>Skill 8</span><span>80%</span></div><div class="skill-track"><div class="skill-fill" style="width:79%"></div></div></div>
    </section>

    <section class="section section--white" style="top:1145px;height:505px">
      <h2 class="sec-title" style="top:43px"><span>Experience</span></h2>
      <p class="sec-desc" style="top:81px">Lorem ipsum dolor sit amet, consectetur adipiscing elit, sed do eiusmod tempor incididunt ut labore et dolore magna aliqua. Quis ipsum suspendisse ultrices gravida.</p>
      <div class="timeline-line" style="top:138px;height:266px"></div>
      <div class="exp" style="top:133px"><span class="exp-date">June 2018 - Present</span><h3 class="exp-title">The standard Lorem Ipsum passage, used since the 1500s</h3><span class="exp-dot"></span><p class="exp-text">Lorem ipsum dolor sit amet, consectetur adipiscing elit, sed do eiusmod tempor incididunt ut labore et dolore magna aliqua. Qs ipsum suspendisse ultrices gravida. Risus commodo viverra maecenas</p></div>
      <div class="exp" style="top:222px"><span class="exp-date">June 2018 - Present</span><h3 class="exp-title">The standard Lorem Ipsum passage, used since the 1500s</h3><span class="exp-dot"></span><p class="exp-text">Lorem ipsum dolor sit amet, consectetur adipiscing elit, sed do eiusmod tempor incididunt ut labore et dolore magna aliqua. Qs ipsum suspendisse ultrices gravida. Risus commodo viverra maecenas</p></div>
      <div class="exp" style="top:311px"><span class="exp-date">June 2018 - Present</span><h3 class="exp-title">The standard Lorem Ipsum passage, used since the 1500s</h3><span class="exp-dot"></span><p class="exp-text">Lorem ipsum dolor sit amet, consectetur adipiscing elit, sed do eiusmod tempor incididunt ut labore et dolore magna aliqua. Qs ipsum suspendisse ultrices gravida. Risus commodo viverra maecenas</p></div>
      <div class="exp" style="top:400px"><span class="exp-date">June 2018 - Present</span><h3 class="exp-title">The standard Lorem Ipsum passage, used since the 1500s</h3><span class="exp-dot"></span><p class="exp-text">Lorem ipsum dolor sit amet, consectetur adipiscing elit, sed do eiusmod tempor incididunt ut labore et dolore magna aliqua. Qs ipsum suspendisse ultrices gravida. Risus commodo viverra maecenas</p></div>
    </section>

    <section class="section section--mist" style="top:1650px;height:260px">
      <h2 class="sec-title" style="top:38px"><span>Latest Blog</span></h2>
      <article class="mini-card" style="left:53px"><div class="date"><i></i>Jan 20,2022</div><h3 class="card-title">The standard Lorem Ipsum passage, used since</h3><p class="card-text">Lorem ipsum dolor simet, consectetur adipid do eiusmod tempor incididunt ut labolore magna aliqua. Quis ipsum suspendices gravida</p><p class="more">Learn More »</p></article>
      <article class="mini-card" style="left:232px"><div class="date"><i></i>Jan 20,2022</div><h3 class="card-title">The standard Lorem Ipsum passage, used since</h3><p class="card-text">Lorem ipsum dolor simet, consectetur adipid do eiusmod tempor incididunt ut labolore magna aliqua. Quis ipsum suspendices gravida</p><p class="more">Learn More »</p></article>
      <article class="mini-card" style="left:411px"><div class="date"><i></i>Jan 20,2022</div><h3 class="card-title">The standard Lorem Ipsum passage, used since</h3><p class="card-text">Lorem ipsum dolor simet, consectetur adipid do eiusmod tempor incididunt ut labolore magna aliqua. Quis ipsum suspendices gravida</p><p class="more">Learn More »</p></article>
    </section>

    <section class="contact">
      <div class="contact-form" role="img" aria-label="Faded photo of a desk with laptop and plans behind the contact form">
        <h2>Get In Touch</h2>
        <div class="field" style="left:59px;top:76px;width:125px">Your Name</div>
        <div class="field" style="left:189px;top:76px;width:126px">Phone</div>
        <div class="field" style="left:59px;top:105px;width:125px">Email address</div>
        <div class="field" style="left:189px;top:105px;width:126px">Subject</div>
        <div class="field" style="left:59px;top:134px;width:256px;height:47px">Message</div>
        <div class="submit">SUBMIT</div>
      </div>
      <div class="contact-info">
        <h2>Contact Us</h2>
        <div class="info-label">OUR VISIT US</div>
        <div class="info-row" style="top:98px"><span class="info-icon"><svg width="11" height="13" viewBox="0 0 11 13"><path d="M5.5 0 C2.5 0 0 2.3 0 5.2 C0 8.6 5.5 13 5.5 13 C5.5 13 11 8.6 11 5.2 C11 2.3 8.5 0 5.5 0Z" fill="#6B429C"/><circle cx="5.5" cy="5" r="2" fill="#fff"/></svg></span><div><small>123 Your Adress Goes Here.<br>CA, 1234567</small></div></div>
        <div class="info-row" style="top:133px"><span class="info-icon"><svg width="11" height="11" viewBox="0 0 11 11"><path d="M2 0 L4 3 L3 4.5 C3.8 6 5 7.2 6.5 8 L8 7 L11 9 L9.5 11 C4.5 10.5 0.5 6.5 0 1.5Z" fill="#6B429C"/></svg></span><div><small>Call Us Today!</small><b>888 - 888 - 8888</b></div></div>
        <div class="info-row" style="top:170px"><span class="info-icon"><svg width="12" height="9" viewBox="0 0 12 9"><rect width="12" height="9" rx="1" fill="#6B429C"/><path d="M0.5 0.8 L6 5 L11.5 0.8" stroke="#fff" fill="none"/></svg></span><div><small>Email Us</small><b>hello@harperstudio.net</b></div></div>
      </div>
    </section>

    <footer class="site-foot" style="top:2164px;height:177px">
      <div class="foot-brand">Logo</div>
      <nav class="foot-nav"><span>Home</span><span>About Me</span><span>Blog</span><span>Resume</span><span>My Work</span><span>Contact</span></nav>
      <p class="foot-copy">© Copyright 2022 Company. All rights reserved.</p>
      <div class="foot-social"><span></span><span></span><span></span><span></span></div>
    </footer>
  </section>

  <!-- BLOG LIST PAGE -->
  <section class="page page--blog">
    <header class="page-head page-head--inner">
      <div class="brand">Logo</div>
      <nav class="nav" style="left:236px"><span>Home</span><span>About Me</span><span class="is-active">Blog</span><span>Resume</span><span>My Work</span><span>Contact</span></nav>
      <h1 class="page-title">Blog</h1>
    </header>

    <article class="post-card" style="left:53px;top:173px"><div class="photo" role="img" aria-label="Photo of a person working at a desk with a laptop" style="background:linear-gradient(135deg,#B98A5E,#6E5444)"></div><div class="date"><i></i>Jan 20,2022</div><h3 class="card-title">The standard Lorem Ipsum passage, used since</h3><p class="card-text">Lorem ipsum dolor simet, consectetur adipid do eiusmod tempor incididunt ut labolore magna aliqua.</p><span class="btn">Learn More</span></article>
    <article class="post-card" style="left:232px;top:173px"><div class="photo" role="img" aria-label="Photo of hands using a laptop and a phone" style="background:linear-gradient(135deg,#D9D4CB,#8E8A85)"></div><div class="date"><i></i>Jan 20,2022</div><h3 class="card-title">The standard Lorem Ipsum passage, used since</h3><p class="card-text">Lorem ipsum dolor simet, consectetur adipid do eiusmod tempor incididunt ut labolore magna aliqua.</p><span class="btn">Learn More</span></article>
    <article class="post-card" style="left:411px;top:173px"><div class="photo" role="img" aria-label="Photo of an artist holding a tablet beside an easel" style="background:linear-gradient(135deg,#5C4A3A,#E8E2D8)"></div><div class="date"><i></i>Jan 20,2022</div><h3 class="card-title">The standard Lorem Ipsum passage, used since</h3><p class="card-text">Lorem ipsum dolor simet, consectetur adipid do eiusmod tempor incididunt ut labolore magna aliqua.</p><span class="btn">Learn More</span></article>
    <article class="post-card" style="left:53px;top:436px"><div class="photo" role="img" aria-label="Photo of colour swatches and sketches on a desk" style="background:linear-gradient(135deg,#4E4A45,#C9A46A)"></div><div class="date"><i></i>Jan 20,2022</div><h3 class="card-title">The standard Lorem Ipsum passage, used since</h3><p class="card-text">Lorem ipsum dolor simet, consectetur adipid do eiusmod tempor incididunt ut labolore magna aliqua.</p><span class="btn">Learn More</span></article>
    <article class="post-card" style="left:232px;top:436px"><div class="photo" role="img" aria-label="Photo of an inline skate on a wooden floor" style="background:linear-gradient(135deg,#8A5A34,#3A2A20)"></div><div class="date"><i></i>Jan 20,2022</div><h3 class="card-title">The standard Lorem Ipsum passage, used since</h3><p class="card-text">Lorem ipsum dolor simet, consectetur adipid do eiusmod tempor incididunt ut labolore magna aliqua.</p><span class="btn">Learn More</span></article>
    <article class="post-card" style="left:411px;top:436px"><div class="photo" role="img" aria-label="Photo of a design workspace with a monitor and colour wheel" style="background:linear-gradient(135deg,#3C3F44,#D8D8DA)"></div><div class="date"><i></i>Jan 20,2022</div><h3 class="card-title">The standard Lorem Ipsum passage, used since</h3><p class="card-text">Lorem ipsum dolor simet, consectetur adipid do eiusmod tempor incididunt ut labolore magna aliqua.</p><span class="btn">Learn More</span></article>

    <div class="pager"><span class="is-current">1</span><span>2</span><span>3</span><span>...</span><span>6</span></div>

    <footer class="site-foot" style="top:803px;height:174px">
      <div class="foot-brand">Logo</div>
      <nav class="foot-nav"><span>Home</span><span>About Me</span><span>Blog</span><span>Resume</span><span>My Work</span><span>Contact</span></nav>
      <p class="foot-copy">© Copyright 2022 Company. All rights reserved.</p>
      <div class="foot-social"><span></span><span></span><span></span><span></span></div>
    </footer>
  </section>

  <!-- SINGLE POST PAGE -->
  <section class="page page--post">
    <header class="page-head page-head--inner">
      <div class="brand">Logo</div>
      <nav class="nav" style="left:236px"><span>Home</span><span>About Me</span><span class="is-active">Blog</span><span>Resume</span><span>My Work</span><span>Contact</span></nav>
      <h1 class="page-title">Blog</h1>
    </header>
    <div class="post-meta"><span>▦ September 11</span><span>◌ Commend</span><span>● admin</span></div>
    <h2 class="post-title">The standard Lorem Ipsum passage,<br>used since</h2>
    <p class="post-body" style="top:239px">Lorem ipsum dolor sit amet, consectetur adipiscing elit, sed do eiusmod tempor incididunt ut labore et dolore magna aliqua. Ut enim ad minim veniam, quis nostrud exercitation ullamco laboris nisi ut aliquip ex ea coodo consequat. Duis aute irure dolor in reprehenderit in voluptate velit esse cillum dolore eu fugiat nulla pariatur. Excepteur sint occaecat cupidatat non proident, sunt in culpa qui officia deserunt mollit anim id est laborum. Sed ut persatis</p>
    <div class="abs" role="img" aria-label="Photo of an artist holding a tablet beside an easel in a bright studio" style="left:56px;top:332px;width:521px;height:272px;background:linear-gradient(120deg,#4A3A2E 0%,#8A6A4E 40%,#E9E4DC 70%,#CFC6B8 100%)"></div>
    <p class="post-body" style="top:630px">Lorem ipsum dolor sit amet, consectetur adipiscing elit, sed do eiusmod tempor incididunt ut labore et dolore magna aliqua. Ut enim ad minim veniam, quis nostrud exercitation ullamco laboris nisi ut aliquip ex ea coodo consequat. Duis aute irure dolor in reprehenderit in voluptate velit esse cillum dolore eu fugiat nulla pariatur. Excepteur sint occaecat cupidatat non proident, sunt in culpa qui officia deserunt mollit anim id est laborum. Sed ut persatis unde omnis iste natus error sit voluptatem accusantium doloremque laudantium, totam rem aperiam, eaque ipsa quae ab illo inventore veritatis et quasi architecto beatae vitae dicta sunt explicabo. Nemo enim ipsam voluptatem quia voluptas sit aspur aut odit aut fugit, sed quia consequuntur magni dolores eos qui ratione voluptatem sequi nesciunt. Neque porro uam est, qui dolorem ipsum quia dolor sit amet, consectetur, adipisci velit, sed quia non numquam eius modi tempora incidunt ut labore et dolore magnam aliquam quaerat voluptatem. Ut enim ad minima veniam, quis nostrum exercitationem ulloorporis suscipit laboriosam, nisi ut aliquid ex ea commodi consequatur? Quis autem vel eum iure reprehenderit qui in ea voluptate velit esse quam nihil molestiae consequatur, vel illum qui dolorem eum fugiat quo voluptas nulla pariatur</p>
    <p class="post-body" style="top:840px">Lorem ipsum dolor sit amet, consectetur adipiscing elit, sed do eiusmod tempor incididunt ut labore et dolore magna aliqua. Ut enim ad minim veniam, quis nostrud exercitation ullamco laboris nisi ut aliquip ex ea coodo consequat. Duis aute irure dolor in reprehenderit in voluptate velit esse cillum dolore eu fugiat nulla pariatur. Excepteur sint occaecat cupidatat non proident, sunt in culpa qui officia deserunt mollit anim id est laborum. Sed ut persatis</p>
    <p class="post-body" style="top:923px">Lorem ipsum dolor sit amet, consectetur adipiscing elit, sed do eiusmod tempor incididunt ut labore et dolore magna aliqua. Ut enim ad minim veniam, quis nostrud exercitation ullamco laboris nisi ut aliquip ex ea coodo consequat. Duis aute irure dolor in reprehenderit in voluptate velit esse cillum dolore eu</p>

    <footer class="site-foot" style="top:1024px;height:171px">
      <div class="foot-brand">Logo</div>
      <nav class="foot-nav"><span>Home</span><span>About Me</span><span>Blog</span><span>Resume</span><span>My Work</span><span>Contact</span></nav>
      <p class="foot-copy">© Copyright 2022 Company. All rights reserved.</p>
      <div class="foot-social"><span></span><span></span><span></span><span></span></div>
    </footer>
  </section>

</div>
</body>
</html>
```